Business Card for TKR, logo files already created

Please, can you assist with creating a Business card the TKR graphics which are already listed on www.tarnkeyrelay.example
The business card should be modern and upmarket, textured designs are welcome. Please feel free to express yourself and be very bold with your design.

Target Market(s)

Cyber Security

Industry/Entity Type

Information Technology

Contact Information for Business Card

Company Name
Name
Title
Mobile
Fax or Tel
email
url

Font styles to use
Serif
Sans Serif

Colors
3277b5
85acd3
ffffff

```html
<!DOCTYPE html>
<html lang="en">
<head>
<meta charset="utf-8">
<title>TKR Business Card</title>
<link href="https://fonts.googleapis.com/css2?family=Michroma&family=Arimo:wght@400&display=swap" rel="stylesheet">
<style>
  :root {
    --backdrop: #6e6e6e;
    --card-navy: #2e3b58;
    --ink-white: #ffffff;
    --ink-soft: #d9dfea;
    --rule: rgba(255,255,255,0.7);
  }
  * { margin: 0; padding: 0; box-sizing: border-box; }
  html, body {
    width: 1200px; height: 800px; overflow: hidden;
    background: var(--backdrop);
  }
  .canvas {
    position: relative; width: 1200px; height: 800px;
    display: flex; align-items: center; justify-content: center; gap: 60px;
  }
  .card {
    position: relative; width: 500px; height: 286px;
    background: var(--card-navy);
    color: var(--ink-white);
    border-radius: 3px;
    box-shadow: 0 10px 24px rgba(0,0,0,0.25);
  }
  /* Front */
  .card-front {
    display: flex; flex-direction: column; align-items: center; justify-content: center;
  }
  .brand-name {
    font-family: "Michroma", sans-serif;
    font-size: 72px; line-height: 1; letter-spacing: 2px;
    color: var(--ink-white);
  }
  .brand-company {
    margin-top: 14px;
    font-family: "Michroma", sans-serif;
    font-size: 18px; letter-spacing: 2px;
  }
  .brand-rule {
    width: 220px; height: 1px; background: var(--rule); margin: 10px 0 8px;
  }
  .brand-tagline {
    font-family: "Arimo", sans-serif;
    font-size: 10px; letter-spacing: 2.5px; color: var(--ink-soft);
  }
  /* Back */
  .holder {
    position: absolute; left: 36px; top: 64px;
    font-family: "Michroma", sans-serif;
  }
  .holder-name { font-size: 17px; letter-spacing: 1px; }
  .holder-title { font-size: 11px; letter-spacing: 1px; margin-top: 4px; }
  .back-mark {
    position: absolute; right: 36px; top: 108px;
    font-family: "Michroma", sans-serif;
    font-size: 46px; line-height: 1; letter-spacing: 1px;
  }
  .contact {
    position: absolute; left: 36px; bottom: 30px;
    list-style: none;
    font-family: "Arimo", sans-serif;
    font-size: 11px; line-height: 1.55; color: var(--ink-soft);
  }
</style>
</head>
<body>
  <main class="canvas">
    <section class="card card-front" aria-label="Card front">
      <div class="brand-name">TKR</div>
      <div class="brand-company">TARNKEY RELAY</div>
      <div class="brand-rule"></div>
      <div class="brand-tagline">INTELLIGENCE - DRIVEN SOLUTIONS</div>
    </section>

    <section class="card card-back" aria-label="Card back">
      <div class="holder">
        <div class="holder-name">JONAH PELL</div>
        <div class="holder-title">CEO/FOUNDER</div>
      </div>
      <div class="back-mark">TKR</div>
      <ul class="contact">
        <li>Tel : 555 014 2738</li>
        <li>Mob : 555 019 4463</li>
        <li>Fax : 555 012 7790</li>
        <li>jonah@tarnkeyrelay.example</li>
        <li>www.tarnkeyrelay.example</li>
      </ul>
    </section>
  </main>
</body>
</html>
```